Sustainably Transforming Education

Company is education services based. early learning through adult and corporate. Focus is national government policy and program design and delivery alongside a research based and academically grounded set of approaches to planning, evaluation, and change management.I am looking for an innovative design position that aligns with the global agendas for innovation, creativity and collaboration at international and national policy levels (ferolu is a name that reflects these qualities - colours need to reflect amythyst in some way). I also need a design that translates from a business card as 1 medium of interaction to a template that can work in word/powerpoint etc to support both stationery as well as a digital strategy across multiple channels (fb/twit/etc)There is no slogan/tag line for the company and their is no logo. I was looking to just leverage the name - have currently played around with various fonts (ending up with cuisine - all lowercase).

Industry/Entity Type

Adult

Contact Information for Business Card

name: ferolu (all lowercase)Chairman: Andrew CrowMobile: +61 418 902 131Web: www.ferolu.comemail: martin.bellamy@ferolu.example

Font styles to use
Script
Other font styles liked:
• cuisine

Colors
e34298
e667a6
33a6d7
aaaaaa

Requirements
Nice to have
• https://www.filecrate.example/sh/qx7wn2rplu4tkez/ZZTmorivPQeLbfNwHyaKcQsRo?dl=0
• Link to the cardmoldo templates used to begin this process....the one with the lines was about people intersecting (collaborating).....the organic shapes one more of a fluid feel of people coming together - the overall shape being largely spherical could represent a "global" feel.....anyway that is how I was thinking about these

```html
<!DOCTYPE html>
<html lang="en">
<head>
<meta charset="utf-8">
<title>ferolu business card</title>
<link rel="stylesheet" href="https://fonts.googleapis.com/css2?family=Lobster&display=swap">
<style>
  :root {
    --canvas: #ffffff;
    --card: #ffffff;
    --edge: #111111;
    --magenta: #e34298;
    --orchid: #e667a6;
    --sky: #33a6d7;
    --grey: #aaaaaa;
  }
  html, body {
    margin: 0;
    padding: 0;
    width: 1200px;
    height: 534px;
    overflow: hidden;
    background: var(--canvas);
  }
  .card {
    position: absolute;
    top: 100px;
    width: 520px;
    height: 320px;
    box-sizing: border-box;
    border: 2px solid var(--edge);
    background: var(--card);
    overflow: hidden;
    font-family: "Lobster", cursive;
  }
  .card--front { left: 57px; }
  .card--back { left: 629px; }
  .card__art {
    position: absolute;
    inset: 0;
    width: 100%;
    height: 100%;
  }
  .wordmark {
    position: absolute;
    margin: 0;
    color: var(--magenta);
    font-weight: 400;
    line-height: 1;
  }
  .card--front .wordmark {
    left: 188px;
    top: 128px;
    font-size: 46px;
  }
  .card--back .wordmark {
    left: 323px;
    top: 43px;
    font-size: 44px;
  }
  .person {
    position: absolute;
    left: 112px;
    top: 92px;
    width: 224px;
    margin: 0;
    color: var(--magenta);
    line-height: 1;
  }
  .person__name {
    display: block;
    font-size: 21px;
    letter-spacing: 0.5px;
  }
  .person__role {
    display: block;
    text-align: right;
    font-size: 18px;
    margin-top: 8px;
  }
  .contact {
    position: absolute;
    margin: 0;
    padding: 0;
    list-style: none;
    font-size: 17px;
    line-height: 1;
  }
  .contact__item {
    position: absolute;
    white-space: nowrap;
  }
  .contact__label { color: var(--grey); }
  .contact__value { color: var(--sky); }
  .contact__item--phone { left: 74px; top: 183px; }
  .contact__item--web { left: 61px; top: 212px; }
  .contact__item--email { left: 50px; top: 240px; }
</style>
</head>
<body>

<section class="card card--front" aria-label="Card front">
  <svg class="card__art" viewBox="0 0 516 316" preserveAspectRatio="none" aria-hidden="true">
    <defs>
      <radialGradient id="front-wisp" cx="1" cy="0.8" r="0.55">
        <stop offset="0" stop-color="#33a6d7" stop-opacity="0.85"/>
        <stop offset="0.45" stop-color="#7cc4e6" stop-opacity="0.4"/>
        <stop offset="1" stop-color="#ffffff" stop-opacity="0"/>
      </radialGradient>
    </defs>
    <rect x="250" y="0" width="266" height="316" fill="url(#front-wisp)" role="img" aria-label="Soft blue flowing organic wisps illustration"/>
    <polygon class="band" points="0,0 146,0 0,312" fill="#e34298"/>
    <polygon class="band band--light" points="52,0 120,0 0,250 0,118" fill="#e667a6"/>
  </svg>
  <h1 class="wordmark">ferolu</h1>
</section>

<section class="card card--back" aria-label="Card back">
  <svg class="card__art" viewBox="0 0 516 316" preserveAspectRatio="none" aria-hidden="true">
    <defs>
      <radialGradient id="back-wisp" cx="1" cy="0.8" r="0.55">
        <stop offset="0" stop-color="#33a6d7" stop-opacity="0.85"/>
        <stop offset="0.45" stop-color="#7cc4e6" stop-opacity="0.4"/>
        <stop offset="1" stop-color="#ffffff" stop-opacity="0"/>
      </radialGradient>
    </defs>
    <rect x="250" y="0" width="266" height="316" fill="url(#back-wisp)" role="img" aria-label="Soft blue flowing organic wisps illustration"/>
    <polygon class="band" points="0,0 146,0 0,312" fill="#e34298"/>
    <polygon class="band band--light" points="52,0 120,0 0,250 0,118" fill="#e667a6"/>
  </svg>
  <h2 class="wordmark">ferolu</h2>
  <p class="person">
    <span class="person__name">Martin BellamyMobile</span>
    <span class="person__role">Chairman</span>
  </p>
  <ul class="contact">
    <li class="contact__item contact__item--phone"><span class="contact__label">Contact: </span><span class="contact__value">+61 427 365 804</span></li>
    <li class="contact__item contact__item--web"><span class="contact__label">web:</span><span class="contact__value">www.ferolu.example</span></li>
    <li class="contact__item contact__item--email"><span class="contact__label">email:</span><span class="contact__value">martin.bellamy@ferolu.example</span></li>
  </ul>
</section>

</body>
</html>
```